Capital Management company needs a web design

We have a domain name and logo but need hosting and design. Please look at the Must-Haves section.

Target Market(s)

banking industry and investors

Industry/Entity Type

Investment

Coding

Coded - Design and coding required

Number of Pages Required

1 page

Font styles to use
Sans Serif

Requirements
Must have
• Picture(s) of skyscraper skyline (can be of Manhattan, Chicago, or any other major city in the USA).
• Please use the three colors of the logo as a backdrop to part of the webpage(s)
Should not have
• No "what our clients say" section
• No pictures of people

```html
<!DOCTYPE html>
<html lang="en">
<head>
<meta charset="utf-8">
<title>Harbor Stone Capital</title>
<link href="https://fonts.googleapis.com/css2?family=Work+Sans:wght@300;400;500;600;700;800&display=swap" rel="stylesheet">
<style>
:root{
  --blue:#3d86c0;
  --blue-bright:#2f7dc4;
  --blue-deep:#1a78c2;
  --grey:#a4a2a9;
  --cream:#f2efec;
  --ink:#5c5c60;
  --muted:#7b7b80;
  --white:#ffffff;
  --dark:#1c1c1e;
}
*{box-sizing:border-box;margin:0;padding:0}
html,body{width:1200px;height:3154px;overflow:hidden}
body{font-family:"Work Sans",Arial,sans-serif;color:var(--ink);background:var(--white);position:relative}
section,header,footer{position:absolute;left:0;width:1200px}
.abs{position:absolute}

/* hero */
.hero{top:0;height:675px;background:linear-gradient(160deg,#2f4a6e 0%,#4a6b8c 35%,#6a7d8f 55%,#9a7e6a 80%,#b57a50 100%);overflow:hidden}
.hero-shade{position:absolute;inset:0;background:linear-gradient(180deg,rgba(20,30,45,.15),rgba(20,30,45,.45))}
.brand{display:flex;align-items:center;gap:10px;color:var(--white);font-weight:600;font-size:21px;letter-spacing:.5px}
.brand-mark{width:16px;height:16px;background:var(--white)}
.hero .brand{left:75px;top:32px}
.nav{left:370px;top:36px;display:flex;gap:26px;font-size:14.5px;color:var(--white);letter-spacing:.3px}
.nav span{padding-bottom:10px}
.nav .active{border-bottom:1.5px solid var(--white)}
.callout{left:994px;top:34px;display:flex;gap:10px;align-items:center;color:var(--white)}
.callout-icon{width:28px;height:26px;background:var(--white);display:flex;align-items:center;justify-content:center}
.callout small{display:block;font-size:10px;line-height:11px}
.callout strong{display:block;font-size:13px;font-weight:700;letter-spacing:.5px}
.hero-title{left:0;width:1200px;top:290px;text-align:center;color:var(--white);font-size:44px;font-weight:600;line-height:45px}
.hero-btn{left:484px;top:410px;width:236px;height:56px;border:1.5px solid var(--white);outline:1px solid rgba(255,255,255,.8);outline-offset:-5px;display:flex;align-items:center;justify-content:center;gap:18px;color:var(--white);font-size:14px;font-weight:600;letter-spacing:.3px}
.hero-arrow{top:315px}
.scroll{left:590px;top:540px}
.dots{left:578px;top:634px;display:flex;gap:4px}
.dots i{width:11px;height:7px;border:1.5px solid var(--white);border-radius:4px}

/* intro */
.intro{top:675px;height:274px;background:var(--grey)}
.intro-head{left:75px;top:60px;width:490px;color:var(--white);font-size:29px;font-weight:800;line-height:30px;text-transform:uppercase;letter-spacing:.3px}
.intro-head em{font-style:normal;color:var(--blue-bright)}
.intro-copy{left:600px;top:63px;width:525px;color:var(--white);font-size:14px;line-height:22.5px}

/* split blocks */
.split{height:600px}
.who{top:949px;background:var(--white)}
.what{top:1849px;background:var(--white)}
.photo{top:0;width:600px;height:600px}
.label{font-size:17.5px;font-weight:700;color:var(--blue);letter-spacing:.5px}
.lead{font-size:29px;font-weight:300;line-height:36px;color:#6a6a70;margin-top:16px}
.body{font-size:14px;line-height:22.5px;color:var(--muted);margin-top:26px;font-weight:300}
.btn{display:inline-flex;align-items:center;justify-content:center;width:150px;height:44px;background:var(--blue);color:var(--white);font-size:14px;font-weight:500;margin-top:28px;letter-spacing:.3px}
.text-col{top:102px;width:470px}

/* features */
.features{top:1549px;height:300px;background:var(--cream);display:flex}
.feature{width:300px;height:300px;text-align:center;position:relative}
.feature svg{position:absolute;left:100px;top:69px}
.feature h3{position:absolute;left:0;width:300px;top:188px;font-size:18px;font-weight:600;color:var(--blue);line-height:22px}
.feature.hl{background:var(--blue);color:var(--white)}
.feature.hl h3{position:static;color:var(--white);padding-top:66px}
.feature.hl p{font-size:14px;line-height:18px;padding:14px 40px 0;font-weight:300}

/* clients */
.clients{top:2449px;height:351px;background:var(--grey);color:var(--white)}
.clients h2{position:absolute;top:57px;width:1200px;text-align:center;font-size:27px;font-weight:600;letter-spacing:.5px}
.client{top:152px;width:320px;text-align:center}
.client h3{font-size:17.5px;font-weight:600;letter-spacing:.3px}
.client p{font-size:14px;line-height:22.5px;font-weight:300;margin-top:16px}

/* footer */
.footer{top:2800px;height:354px}
.footer-info{left:0;top:0;width:600px;height:295px;background:var(--blue-deep);color:var(--white)}
.footer-info .brand{left:75px;top:40px}
.contact-line{left:75px;display:flex;gap:16px;align-items:center}
.contact-line small{display:block;font-size:10.5px;font-weight:600}
.contact-line strong{display:block;font-size:15px;font-weight:600;letter-spacing:.4px}
.contact-line .em{font-size:13.5px;font-weight:400}
.socials{left:75px;top:237px;display:flex;gap:6px}
.socials i{width:30px;height:30px;border-radius:50%;background:rgba(255,255,255,.25)}
.legal{left:0;top:295px;width:600px;height:59px;background:var(--dark);color:#666;font-size:10px;display:flex;justify-content:space-between;align-items:center;padding:0 28px 0 75px}
.form-panel{left:600px;top:0;width:600px;height:354px;background:var(--blue)}
.form-panel h2{position:absolute;left:51px;top:42px;color:var(--white);font-size:30px;font-weight:600}
.field{position:absolute;background:var(--white);border:1px solid #d7dbe0;font-size:11px;color:#777;padding:12px 12px}
.submit{position:absolute;left:51px;top:268px;width:474px;height:42px;background:var(--blue-bright);color:var(--white);font-size:14px;font-weight:700;display:flex;align-items:center;justify-content:center;letter-spacing:.5px}
</style>
</head>
<body>

<header class="hero">
  <div class="abs" role="img" aria-label="Photograph of a downtown skyscraper skyline at dusk with a river and highway" style="inset:0"></div>
  <div class="hero-shade"></div>
  <div class="abs brand"><span class="brand-mark"></span>Harbor Stone Capital</div>
  <nav class="abs nav">
    <span class="active">Home</span><span>Who we are</span><span>What we do</span><span>Our clients</span><span>Contact</span>
  </nav>
  <div class="abs callout">
    <span class="callout-icon"><svg width="18" height="16" viewBox="0 0 18 16"><path d="M2 5c0-2 3-3 7-3s7 1 7 3v1h-3V4.5H5V6H2z M4 7h10l2 7H2z" fill="#2f5f9a"/><circle cx="9" cy="10.5" r="2" fill="#fff"/></svg></span>
    <div><small>Call us now</small><strong>123-456 7890</strong></div>
  </div>
  <svg class="abs hero-arrow" style="left:48px" width="30" height="46" viewBox="0 0 30 46"><path d="M26 3L6 23l20 20" stroke="#fff" stroke-width="5" fill="none"/></svg>
  <svg class="abs hero-arrow" style="left:1124px" width="30" height="46" viewBox="0 0 30 46"><path d="M4 3l20 20L4 43" stroke="#fff" stroke-width="5" fill="none"/></svg>
  <h1 class="abs hero-title">Lorem Ipsum is simply dummy<br>text of the typeset industry.</h1>
  <div class="abs hero-btn">Contact us now
    <svg width="24" height="10" viewBox="0 0 24 10"><path d="M0 5h22M17 1l5 4-5 4" stroke="#fff" stroke-width="1.3" fill="none"/></svg>
  </div>
  <svg class="abs scroll" width="20" height="46" viewBox="0 0 20 46"><rect x="2" y="1" width="16" height="26" rx="8" stroke="#fff" stroke-width="1.6" fill="none"/><path d="M5 35l5 5 5-5" stroke="#fff" stroke-width="1.6" fill="none"/></svg>
  <div class="abs dots"><i></i><i></i><i></i></div>
</header>

<section class="intro">
  <h2 class="abs intro-head">Lorem Ipsum is simply dummy text of the <em>printing and typesetting</em> industry Lorem Ipsum has been the industry's standard</h2>
  <p class="abs intro-copy">Lorem Ipsum is simply dummy text of the printing and typesetting industry. Lorem Ipsum has been the industry's standard dummy text ever since the 1500s, when an unknown printer took a galley of type and scrambled it to make a type specimen book. It has survived not only five centuries, but also the leap into electronic typesetting, remaining essentially unchanged.</p>
</section>

<section class="split who">
  <div class="abs text-col" style="left:75px">
    <div class="label">WHO WE ARE</div>
    <p class="lead">Lorem Ipsum is simply dummy text of the printing and typesetting industry. Lorem Ipsum has been text ever since the 1500s.</p>
    <p class="body">Lorem Ipsum is simply dummy text of the printing and typesetting industry. Lorem Ipsum has been the industry's standard dummy text ever since the 1500s, when an unknown printer took a galley of type and scrambled it to make a type specimen book. It has survived not only five centuries, but also the leap into electronic typesetting, remaining essentially unchanged.</p>
    <span class="btn">Contact Us</span>
  </div>
  <div class="abs photo" role="img" aria-label="Photograph of hands holding a smartphone showing the website" style="left:600px;background:linear-gradient(135deg,#e8eef3 0%,#c9d3dc 45%,#8a98a6 75%,#d7c1ad 100%)"></div>
</section>

<section class="features">
  <div class="feature">
    <svg width="100" height="100" viewBox="0 0 100 100"><circle cx="50" cy="50" r="50" fill="#3d86c0"/><circle cx="50" cy="50" r="17" stroke="#fff" stroke-width="8" fill="none" stroke-dasharray="9 4.3"/><circle cx="50" cy="50" r="12" stroke="#fff" stroke-width="7" fill="none"/></svg>
    <h3>Sed ut perspiciatis unde<br>omnis iste natus error</h3>
  </div>
  <div class="feature">
    <svg width="100" height="100" viewBox="0 0 100 100"><circle cx="50" cy="50" r="50" fill="#3d86c0"/><circle cx="50" cy="50" r="17" stroke="#fff" stroke-width="8" fill="none" stroke-dasharray="9 4.3"/><circle cx="50" cy="50" r="12" stroke="#fff" stroke-width="7" fill="none"/></svg>
    <h3>Sed ut perspiciatis unde<br>omnis iste natus error</h3>
  </div>
  <div class="feature hl">
    <h3>Sed ut perspiciatis unde<br>omnis iste natus error</h3>
    <p>Neque porro quisquam est, qui dolorem ipsum quia dolor sit amet, consectetur, adipisci velit, sed quia non numquam eius modi tempora incidunt ut labore et dolore magnam aliquam</p>
  </div>
  <div class="feature">
    <svg width="100" height="100" viewBox="0 0 100 100"><circle cx="50" cy="50" r="50" fill="#3d86c0"/><circle cx="50" cy="50" r="17" stroke="#fff" stroke-width="8" fill="none" stroke-dasharray="9 4.3"/><circle cx="50" cy="50" r="12" stroke="#fff" stroke-width="7" fill="none"/></svg>
    <h3>Sed ut perspiciatis unde<br>omnis iste natus error</h3>
  </div>
</section>

<section class="split what">
  <div class="abs photo" role="img" aria-label="Photograph of a desk with a finance sketch on paper, a laptop keyboard, a leather notebook and a clipboard" style="left:0;background:linear-gradient(160deg,#cfe2ea 0%,#b9d3de 50%,#a9c6d3 100%)"></div>
  <div class="abs text-col" style="left:667px">
    <div class="label">WHAT WE DO</div>
    <p class="lead">Lorem Ipsum is simply dummy text of the printing and typesetting industry. Lorem Ipsum has been text ever since the 1500s.</p>
    <p class="body">Lorem Ipsum is simply dummy text of the printing and typesetting industry. Lorem Ipsum has been the industry's standard dummy text ever since the 1500s, when an unknown printer took a galley of type and scrambled it to make a type specimen book. It has survived not only five centuries, but also the leap into electronic typesetting, remaining essentially unchanged.</p>
    <span class="btn">Contact Us</span>
  </div>
</section>

<section class="clients">
  <h2>OUR CLIENTS</h2>
  <div class="abs client" style="left:89px"><h3>BUSINESS ADVISORS</h3><p>Lorem Ipsum is simply dummy text of the printing and typesetting industry. Lorem Ipsum has been the industry's standard dummy text ever since the 1500s, when an unknown</p></div>
  <div class="abs client" style="left:440px"><h3>BUSINESS OWNERS</h3><p>Lorem Ipsum is simply dummy text of the printing and typesetting industry. Lorem Ipsum has been the industry's standard dummy text ever since the 1500s, when an unknown</p></div>
  <div class="abs client" style="left:790px"><h3>INVESTORS</h3><p>Lorem Ipsum is simply dummy text of the printing and typesetting industry. Lorem Ipsum has been the industry's standard dummy text ever since the 1500s, when an unknown</p></div>
</section>

<footer class="footer">
  <div class="abs footer-info">
    <div class="abs brand"><span class="brand-mark"></span>Harbor Stone Capital</div>
    <div class="abs contact-line" style="top:120px">
      <svg width="24" height="22" viewBox="0 0 24 22"><path d="M2 7c0-3 4-5 10-5s10 2 10 5v2h-4V6.5H6V9H2z M5 10h14l3 10H2z" fill="#fff"/><circle cx="12" cy="15" r="2.6" fill="#1a78c2"/></svg>
      <div><small>PHONE</small><strong>123-456 7890</strong></div>
    </div>
    <div class="abs contact-line" style="top:162px">
      <svg width="24" height="18" viewBox="0 0 24 18"><rect x="1" y="1" width="22" height="16" stroke="#fff" stroke-width="2" fill="none"/><path d="M1 2l11 8 11-8" stroke="#fff" stroke-width="2" fill="none"/></svg>
      <div><small>EMAIL</small><strong class="em">info@harborstonecapital.com</strong></div>
    </div>
    <div class="abs socials"><i></i><i></i><i></i><i></i><i></i></div>
  </div>
  <div class="abs legal"><span>© Copyright 2019 Company Name. All rights reserved.</span><span>Privacy Policy</span></div>
  <div class="abs form-panel">
    <h2>Contact Us</h2>
    <div class="field" style="left:51px;top:97px;width:234px;height:36px">First Name</div>
    <div class="field" style="left:291px;top:97px;width:234px;height:36px">Last Name</div>
    <div class="field" style="left:51px;top:140px;width:234px;height:36px">Phone</div>
    <div class="field" style="left:291px;top:140px;width:234px;height:36px">Email</div>
    <div class="field" style="left:51px;top:183px;width:474px;height:76px">Message</div>
    <div class="submit">SUBMIT</div>
  </div>
</footer>

</body>
</html>
```